landscaping core flute signs

I need core flutes created with business name and a few extra dot points for putting on fences for job sites 120cm x 120cm approx.
I want our old ones information with the new L logo and colour palette

```html
<!DOCTYPE html>
<html lang="en">
<head>
<meta charset="utf-8">
<title>Grounded Form – Site Sign</title>
<link rel="stylesheet" href="https://fonts.googleapis.com/css2?family=Montserrat:wght@500;600;700&display=swap">
<style>
  :root {
    --canvas-bg: #ececec;
    --sign-bg: #ffffff;
    --ink: #1a1a1a;
    --ink-soft: #333333;
    --leaf: #5b8c56;
  }
  * { margin: 0; padding: 0; box-sizing: border-box; }
  html, body {
    width: 1200px;
    height: 829px;
    overflow: hidden;
    background: var(--canvas-bg);
    font-family: "Montserrat", Arial, sans-serif;
  }
  .sign {
    position: absolute;
    left: 185.5px;
    top: 0;
    width: 796px;
    height: 796px;
    background: var(--sign-bg);
    transform: scale(1.0414);
    transform-origin: top left;
  }
  .brand-mark {
    position: absolute;
    left: 303px;
    top: 25px;
    width: 190px;
    height: 190px;
    border-radius: 50%;
    background: var(--leaf);
  }
  .brand-name {
    position: absolute;
    left: 0;
    width: 796px;
    top: 246px;
    text-align: center;
    font-size: 50px;
    font-weight: 600;
    letter-spacing: 2px;
    color: var(--ink);
  }
  .tagline {
    position: absolute;
    left: 0;
    width: 796px;
    top: 342px;
    text-align: center;
    font-size: 15px;
    font-weight: 500;
    letter-spacing: 4px;
    color: var(--leaf);
  }
  .services {
    position: absolute;
    left: 180px;
    top: 396px;
    list-style: none;
  }
  .services li {
    display: flex;
    align-items: center;
    height: 67px;
    font-size: 33px;
    font-weight: 500;
    color: var(--ink-soft);
  }
  .services li::before {
    content: "";
    width: 16px;
    height: 16px;
    border-radius: 50%;
    background: var(--leaf);
    margin-right: 12px;
  }
  .phone {
    position: absolute;
    left: 0;
    width: 796px;
    top: 590px;
    text-align: center;
    font-size: 70px;
    font-weight: 700;
    color: var(--ink-soft);
  }
  .email {
    position: absolute;
    left: 0;
    width: 796px;
    top: 686px;
    text-align: center;
    font-size: 36px;
    font-weight: 600;
    color: var(--ink-soft);
  }
  .licence {
    position: absolute;
    right: 43px;
    top: 738px;
    font-size: 20px;
    font-weight: 700;
    color: var(--ink-soft);
    letter-spacing: 0.5px;
  }
</style>
</head>
<body>
  <main class="sign">
    <div class="brand-mark" aria-hidden="true"></div>
    <h1 class="brand-name">GROUNDED FORM</h1>
    <p class="tagline">STRUCTURAL LANDSCAPING</p>
    <ul class="services">
      <li>Paving &amp; Concreting</li>
      <li>Fencing &amp; Retaining</li>
      <li>Desgin &amp; Construct</li>
    </ul>
    <p class="phone">0412 583 904</p>
    <p class="email">sam@groundedform.com</p>
    <p class="licence">QBSA:&nbsp; 1427316</p>
  </main>
</body>
</html>
```